**** Business card design for VoltaNode ****

For my ICT company VoltaNode I need I need a business card design.

We design, build and host web-applications and we have our own CMS product.

Some good examples are attached.

The information should be:
Joris Tielenburg
Managing director
E: j.tielenburg@voltanode-example.nl
M: +31(0)6 57218064
T: +31(0)40 7249305
W: www.voltanode-example.nl

Address:
Berend Vlootweg 27
5612 KT Eindhoven

Industry/Entity Type

Business

Requirements
Must have
• - Use logo (see attachments)
- Double sided
- Distinctive
Nice to have
• - Place for a statement on the back-side: "Designed with knowledge, built with passion"
- HTML code (or Wordpress)
- Dark (black or dark-gray) side
- Small simple images for telephone, e-mail en Url.
- QR code (only if not disturbing), not required, just an option

```html
<!DOCTYPE html>
<html lang="en">
<head>
<meta charset="utf-8">
<title>VoltaNode — Business Card</title>
<link href="https://fonts.googleapis.com/css2?family=Open+Sans:wght@400;600&family=Arimo:wght@400;700&display=swap" rel="stylesheet">
<style>
  :root {
    --backdrop: #e9e6e1;
    --card-black: #000000;
    --card-white: #ffffff;
    --brand-blue: #2aa9e8;
    --cyan: #6fe3f0;
    --silver: #9fb0b8;
    --slate: #6d7f88;
    --ink: #111111;
    --ink-soft: #444444;
    --paper-text: #ffffff;
  }
  html, body {
    margin: 0;
    padding: 0;
    width: 1200px;
    height: 1000px;
    overflow: hidden;
    background: var(--backdrop);
  }
  .canvas {
    position: relative;
    width: 1200px;
    height: 1000px;
  }
  .card {
    position: absolute;
    width: 751px;
    height: 444px;
    overflow: hidden;
    box-shadow: 0 6px 18px rgba(0,0,0,0.25);
  }

  /* Front side */
  .card-front {
    left: 53px;
    top: 36px;
    background: var(--card-black);
  }
  .brand {
    position: absolute;
    display: flex;
    align-items: center;
    gap: 18px;
    font-family: "Open Sans", sans-serif;
    font-weight: 400;
    white-space: nowrap;
  }
  .brand-dot {
    border-radius: 50%;
    background: var(--brand-blue);
    flex: none;
  }
  .card-front .brand {
    left: 170px;
    top: 170px;
    font-size: 58px;
    color: var(--silver);
  }
  .card-front .brand-dot { width: 70px; height: 70px; }
  .tagline {
    position: absolute;
    left: 0;
    right: 0;
    top: 336px;
    text-align: center;
    font-family: "Open Sans", sans-serif;
    font-size: 26px;
    color: var(--cyan);
  }
  .front-url {
    position: absolute;
    left: 0;
    right: 0;
    top: 402px;
    text-align: center;
    font-family: "Open Sans", sans-serif;
    font-size: 17px;
    color: var(--cyan);
  }

  /* Back side */
  .card-back {
    left: 393px;
    top: 507px;
    background: var(--card-black);
  }
  .back-curve {
    position: absolute;
    inset: 0;
  }
  .card-back .brand {
    left: 365px;
    top: 94px;
    font-size: 44px;
    color: var(--slate);
  }
  .card-back .brand-dot { width: 56px; height: 56px; }
  .contact {
    position: absolute;
    left: 56px;
    top: 156px;
    font-family: "Open Sans", sans-serif;
    font-size: 16px;
    line-height: 22px;
    color: var(--paper-text);
  }
  .address { margin: 0 0 32px 0; }
  .contact-row {
    display: flex;
    align-items: center;
    gap: 6px;
    height: 23px;
    font-size: 15px;
  }
  .contact-group { margin-bottom: 30px; }
  .contact-row svg { width: 16px; height: 16px; flex: none; }
  .person {
    position: absolute;
    right: 51px;
    top: 252px;
    text-align: right;
  }
  .person-name {
    font-family: "Arimo", sans-serif;
    font-weight: 700;
    font-size: 30px;
    line-height: 32px;
    color: var(--ink);
  }
  .person-role {
    font-family: "Arimo", sans-serif;
    font-size: 18px;
    line-height: 20px;
    color: var(--ink-soft);
  }
</style>
</head>
<body>
<main class="canvas">

  <section class="card card-front" aria-label="Business card front">
    <div class="brand">
      <span class="brand-dot"></span>
      <span class="brand-name">VoltaNode</span>
    </div>
    <p class="tagline" style="margin:0">Designed with knowledge, built with passion</p>
    <p class="front-url" style="margin:0">www.voltanode-example.nl</p>
  </section>

  <section class="card card-back" aria-label="Business card back">
    <svg class="back-curve" viewBox="0 0 751 444" width="751" height="444" aria-hidden="true">
      <path d="M333 0 C 240 90, 220 330, 527 444 L 751 444 L 751 0 Z" fill="#ffffff"/>
    </svg>

    <div class="brand">
      <span class="brand-dot"></span>
      <span class="brand-name">VoltaNode</span>
    </div>

    <div class="contact">
      <p class="address">Berend Vlootweg 27<br>5612 KT Eindhoven</p>

      <div class="contact-group">
        <div class="contact-row">
          <svg viewBox="0 0 16 16" aria-hidden="true"><path d="M4 1.5 L6.5 4.5 L5 6.2 C6 8.3 7.7 10 9.8 11 L11.5 9.5 L14.5 12 L13 14.3 C7.5 14 2 8.5 1.7 3 Z" fill="#fff"/></svg>
          <span>+31(0)40 7249305</span>
        </div>
        <div class="contact-row">
          <svg viewBox="0 0 16 16" aria-hidden="true"><rect x="4" y="1" width="8" height="14" rx="1.5" fill="none" stroke="#fff" stroke-width="1.6"/><rect x="6" y="3.5" width="4" height="5" fill="#fff"/><circle cx="8" cy="12" r="1" fill="#fff"/></svg>
          <span>+31(0)6 57218064</span>
        </div>
      </div>

      <div class="contact-row">
        <svg viewBox="0 0 16 16" aria-hidden="true"><rect x="1.5" y="4" width="13" height="9" fill="none" stroke="#fff" stroke-width="1.5"/><path d="M1.5 4 L8 9 L14.5 4" fill="none" stroke="#fff" stroke-width="1.5"/></svg>
        <span>j.tielenburg@voltanode-example.nl</span>
      </div>
      <div class="contact-row">
        <svg viewBox="0 0 16 16" aria-hidden="true"><circle cx="8" cy="8" r="6.5" fill="none" stroke="#fff" stroke-width="1.4"/><ellipse cx="8" cy="8" rx="3" ry="6.5" fill="none" stroke="#fff" stroke-width="1.2"/><path d="M1.5 8 H14.5 M2.8 4.5 H13.2 M2.8 11.5 H13.2" stroke="#fff" stroke-width="1.1"/></svg>
        <span>www.voltanode-example.nl</span>
      </div>
    </div>

    <div class="person">
      <div class="person-name">Joris Tielenburg</div>
      <div class="person-role">Managing director</div>
    </div>
  </section>

</main>
</body>
</html>
```